Willowmere Cremations Business Cards

To create a business card for my company Willowmere Cremations. Remember it is a cremation company.
We want to make sure people have a business card and information. Something modern, professional
100% Online
Prices starting at $695 all-inclusive (prices subject to change without notice).
A business card is the first point of contact with the prospective client.

Contact Information for Business Card

(305) 472-8163
www.WillowmereCremationsMiami.example
willowmerecremations@mailbox.example

Requirements
Must have
• 100% Online
Prices starting at $695 all-inclusive (prices subject to change without notice)

(305) 472-8163

Must match logo style
Should not have
• No black backgrounds. Please only use the white, orange and blue from the logo

```html
<!DOCTYPE html>
<html lang="en">
<head>
<meta charset="UTF-8">
<title>Willowmere Cremations – Business Card Back</title>
<link rel="stylesheet" href="https://fonts.googleapis.com/css2?family=Jost:wght@600&family=Didact+Gothic&display=swap">
<style>
  :root {
    --card-white: #ffffff;
    --sunset-orange: #f59752;
    --frame-orange: #f08a45;
    --brand-blue: #1f4e8c;
  }
  html, body {
    margin: 0;
    padding: 0;
    width: 1200px;
    height: 686px;
    overflow: hidden;
    background: var(--card-white);
  }
  .card {
    position: relative;
    width: 1200px;
    height: 686px;
    background: var(--card-white);
    overflow: hidden;
  }
  .card-shapes {
    position: absolute;
    inset: 0;
    width: 1200px;
    height: 686px;
  }
  .contact {
    position: absolute;
    left: 0;
    right: 0;
    top: 298px;
    text-align: center;
    color: var(--brand-blue);
  }
  .contact-phone {
    margin: 0;
    font-family: "Jost", sans-serif;
    font-weight: 600;
    font-size: 52px;
    line-height: 1;
    letter-spacing: 0.16em;
    padding-left: 0.16em;
  }
  .contact-web,
  .contact-email {
    margin: 0;
    font-family: "Didact Gothic", sans-serif;
    font-size: 24px;
    line-height: 1.5;
    letter-spacing: 0.12em;
    padding-left: 0.12em;
  }
  .contact-web { margin-top: 20px; }
  .offer {
    margin-top: 30px;
  }
  .offer-online {
    margin: 0;
    font-family: "Jost", sans-serif;
    font-weight: 600;
    font-size: 20px;
    line-height: 1.3;
    letter-spacing: 0.2em;
    padding-left: 0.2em;
    color: var(--frame-orange);
  }
  .offer-price {
    margin: 6px 0 0;
    font-family: "Didact Gothic", sans-serif;
    font-size: 19px;
    line-height: 1.4;
    letter-spacing: 0.08em;
    padding-left: 0.08em;
  }
  .offer-note {
    margin: 2px 0 0;
    font-family: "Didact Gothic", sans-serif;
    font-size: 14px;
    line-height: 1.4;
    letter-spacing: 0.08em;
    padding-left: 0.08em;
  }
</style>
</head>
<body>
  <main class="card">
    <svg class="card-shapes" viewBox="0 0 1200 686" aria-hidden="true">
      <path class="corner-top-right" d="M1029 0 Q1160 40 1200 146 L1200 0 Z" fill="var(--sunset-orange)"/>
      <path class="corner-bottom-left" d="M0 429 Q45 600 243 686 L0 686 Z" fill="var(--sunset-orange)"/>
      <g class="frame-lines" stroke="var(--frame-orange)" stroke-width="1.8" fill="none">
        <line x1="27" y1="19" x2="1036" y2="19"/>
        <line x1="27" y1="19" x2="27" y2="449"/>
        <line x1="1173" y1="147" x2="1173" y2="667"/>
        <line x1="247" y1="667" x2="1173" y2="667"/>
      </g>
    </svg>
    <section class="contact">
      <p class="contact-phone">(305) 472-8163</p>
      <p class="contact-web">www.willowmerecremationsmiami.example</p>
      <p class="contact-email">willowmerecremations@mailbox.example</p>
      <div class="offer">
        <p class="offer-online">100% ONLINE</p>
        <p class="offer-price">Prices starting at $695 all-inclusive</p>
        <p class="offer-note">(prices subject to change without notice)</p>
      </div>
    </section>
  </main>
</body>
</html>
```